Wealth management Facebook Advertisement

Hello, we are trying to capture more leads to our online booking link through Facebook advertisement. We want an attractive modern design to get more clients and catch the attention of high net-worth clients. We deal with high-net-worth retirees, business owners, farmers, and wealth transfer. We offer high-net-worth client solutions that cover Financial Planning, Retirement and Estate Planning, Investment Planning, Tax Planning, and Insurance Planning. The final design that we would be looking for is modern and eye-catching and makes the prospective clients want to click our meeting link to schedule an introductory consultation.

We are in the Wealth Management / Financial Planning industry

Our online booking link Is the following :

https://calendar.bookvantor.net/owa/calendar/CarlMorrowPartnersVLPrivateWealth@velmoracapital.net/bookings/

Our current Facebook page is the following:

https://www.socialquelt.net/MorrowPrivateWealth

Please ask any further questions for needed information for creating design

```html
<!DOCTYPE html>
<html lang="en">
<head>
<meta charset="utf-8">
<title>VL Private Wealth – Financial Future Ad</title>
<link rel="stylesheet" href="https://fonts.googleapis.com/css2?family=Asap:wght@400;600;700&family=Montserrat:wght@300;600&family=Bebas+Neue&display=swap">
<style>
  :root {
    --page-bg: #d3d3d3;
    --ad-bg: #ffffff;
    --navy: #10244f;
    --brand-blue: #1f64c8;
    --link-blue: #2a6ccf;
    --button-blue: #1a5fc4;
    --button-text: #ffffff;
    --photo-warm: #b89a7c;
    --photo-light: #e9e2d8;
    --photo-cool: #2f5fae;
  }
  * { margin: 0; padding: 0; box-sizing: border-box; }
  html, body {
    width: 1200px; height: 1004px; overflow: hidden;
    background: var(--page-bg);
  }
  .ad {
    position: absolute; left: 130px; top: 32px;
    width: 940px; height: 940px;
    background: var(--ad-bg);
    overflow: hidden;
    box-shadow: 0 6px 18px rgba(0,0,0,0.18);
  }
  .ad-art { position: absolute; inset: 0; }

  .brand {
    position: absolute; top: 48px; left: 0; right: 0;
    display: flex; justify-content: center; align-items: center; gap: 12px;
  }
  .brand-mark { width: 34px; height: 34px; background: var(--navy); }
  .brand-name {
    font-family: "Montserrat", sans-serif; font-weight: 600;
    font-size: 15px; line-height: 1.2; color: var(--navy);
    text-transform: uppercase; letter-spacing: 0.3px;
  }

  .headline { position: absolute; top: 158px; left: 0; right: 0; text-align: center; }
  .headline-lead {
    font-family: "Montserrat", sans-serif; font-weight: 300;
    font-size: 40px; color: var(--navy); letter-spacing: 0.5px;
    white-space: nowrap;
  }
  .headline-main {
    font-family: "Asap", sans-serif; font-weight: 700;
    font-size: 92px; line-height: 1; color: var(--brand-blue);
    letter-spacing: 1px; margin-top: 2px; white-space: nowrap;
  }

  .services { position: absolute; top: 320px; left: 0; right: 0; text-align: center; }
  .services-title {
    font-family: "Montserrat", sans-serif; font-weight: 600;
    font-size: 22px; color: var(--navy); margin-bottom: 10px;
  }
  .services-row {
    display: flex; justify-content: center; gap: 24px;
    font-family: "Asap", sans-serif; font-size: 22px; color: var(--link-blue);
    line-height: 36px; white-space: nowrap;
  }

  .cta {
    position: absolute; top: 828px; left: 188px;
    width: 564px; height: 62px; border-radius: 31px;
    background: var(--button-blue);
    display: flex; align-items: center; justify-content: center; gap: 14px;
    font-family: "Bebas Neue", sans-serif; font-weight: 400;
    font-size: 48px; line-height: 1; color: var(--button-text); text-transform: uppercase;
    white-space: nowrap; padding-top: 4px;
  }
  .cta svg { width: 32px; height: 32px; margin-top: -4px; }
</style>
</head>
<body>
  <div class="ad">
    <svg class="ad-art" viewBox="0 0 940 940">
      <defs>
        <linearGradient id="topHaze" x1="0" y1="0" x2="1" y2="0">
          <stop offset="0" stop-color="#e4e6ea"/>
          <stop offset="0.5" stop-color="#ffffff"/>
          <stop offset="1" stop-color="#e7e8ec"/>
        </linearGradient>
        <linearGradient id="photoTone" x1="0" y1="0" x2="1" y2="0">
          <stop offset="0" stop-color="#c9d3e6"/>
          <stop offset="0.25" stop-color="#b89a7c"/>
          <stop offset="0.6" stop-color="#e9e2d8"/>
          <stop offset="1" stop-color="#c4a98a"/>
        </linearGradient>
        <linearGradient id="photoFade" x1="0" y1="0" x2="0" y2="1">
          <stop offset="0" stop-color="#ffffff" stop-opacity="0"/>
          <stop offset="0.45" stop-color="#2f5fae" stop-opacity="0.35"/>
          <stop offset="0.8" stop-color="#ffffff" stop-opacity="0.85"/>
          <stop offset="1" stop-color="#ffffff" stop-opacity="1"/>
        </linearGradient>
      </defs>
      <rect width="940" height="440" fill="url(#topHaze)" role="img" aria-label="Faint background photo of hands counting coins on a desk"/>
      <g role="img" aria-label="Photo of a smiling senior couple meeting with a financial advisor">
        <path d="M0 418 Q470 500 940 418 L940 940 L0 940 Z" fill="url(#photoTone)"/>
        <path d="M0 418 Q470 500 940 418 L940 940 L0 940 Z" fill="url(#photoFade)"/>
      </g>
    </svg>

    <div class="brand">
      <span class="brand-mark"></span>
      <div class="brand-name">VL Private Wealth Management<br>Carl Morrow &amp; Partners</div>
    </div>

    <div class="headline">
      <div class="headline-lead">LET’S ACHIEVE A STRONGER</div>
      <div class="headline-main">Financial Future</div>
    </div>

    <div class="services">
      <div class="services-title">SERVICES WE OFFER:</div>
      <div class="services-row">
        <span>Financial Planning</span><span>Investment Planning</span><span>Insurance Planning</span>
      </div>
      <div class="services-row">
        <span>Tax Planning</span><span>Retirement &amp; Estate Planning</span>
      </div>
    </div>

    <div class="cta">
      <span>Book your consultation now</span>
      <svg viewBox="0 0 34 34" aria-hidden="true">
        <circle cx="17" cy="17" r="14" fill="none" stroke="#fff" stroke-width="3"/>
        <path d="M17 9 V23 M11 17 L17 23 L23 17" fill="none" stroke="#fff" stroke-width="3" stroke-linecap="round" stroke-linejoin="round"/>
      </svg>
    </div>
  </div>
</body>
</html>
```